A empresa queria:
" O Grupo VELQUAR busca a conversão das mais inovadoras tecnologias nas soluções mais impactantes para o mercado. Nesta perspectiva, a VELQUAR BIOTECNOLOGIA ANIMAL constitui nosso segmento encarregado por transformar o conhecimento científico em bioferramentas inteligentes que agreguem o máximo valor às biotecnologias da reprodução tornando-as cada vez mais produtivas e lucrativas. Atuamos há mais de 10 anos no contexto da Reprodução Animal, dentro e fora do Brasil, executando tanto biotecnologias tradicionais, como a IATF (Inseminação Artificial em Tempo Fixo) e a SOV/TE (Superovulação e Transferência de Embriões), quanto bioferramentas modernas e de altíssimo impacto como a produção de embriões FIV (Fecundados In Vitro) e a clonagem animal. Nossa missão é contribuir decisivamente para o aprimoramento e emprego cada vez mais eficiente, rentável e satisfatório das biotecnologias da reprodução. Estruturado em valores como integridade, excelência e trabalho em equipe, constituímos uma companhia altamente amigável e absolutamente confiável para a execução das biotecnologias mais modernas com vistas, sempre, à plena satisfação do cliente. "

```html
<!DOCTYPE html>
<html lang="pt-BR">
<head>
<meta charset="utf-8">
<title>VELQUAR — FIV Bovinos</title>
<link href="https://fonts.googleapis.com/css2?family=Raleway:wght@300;400;600;700;800&display=swap" rel="stylesheet">
<style>
  :root{
    --green:#5c9e3a;
    --green-dark:#4a8a2c;
    --ink:#3a3a3a;
    --grey:#6d6d6d;
    --white:#ffffff;
  }
  *{box-sizing:border-box;margin:0;padding:0}
  html,body{width:1200px;height:1200px;overflow:hidden;background:var(--white);font-family:'Raleway',sans-serif;color:var(--ink)}
  .page{position:relative;width:1200px;height:1200px}

  .site-header{position:absolute;top:40px;left:150px;right:150px;display:flex;align-items:center;justify-content:space-between}
  .brand{display:flex;align-items:center;gap:12px}
  .brand-mark{width:34px;height:34px;background:var(--green)}
  .brand-text{display:flex;flex-direction:column;color:var(--green);font-weight:700;line-height:1}
  .brand-name{font-size:32px;letter-spacing:1px}
  .brand-tag{font-size:9px;letter-spacing:1.5px;margin-top:4px}
  .main-nav{display:flex;align-items:center;gap:30px;font-size:13px;font-weight:800;color:var(--ink)}
  .main-nav .active{border:1.5px solid var(--ink);border-radius:3px;padding:4px 8px}
  .lang{display:flex;align-items:center;gap:5px;color:var(--grey);font-weight:600;font-size:11px}
  .lang-dot{width:12px;height:8px;background:var(--green)}

  .side-nav{position:absolute;top:258px;left:150px;list-style:none;font-size:15px;font-weight:800;line-height:1.7}
  .side-nav .current{color:var(--green)}

  .intro{position:absolute;top:150px;left:330px;width:720px}
  .intro h1{font-size:58px;font-weight:800;letter-spacing:1px;color:var(--ink)}
  .intro h1 span{color:var(--green)}
  .intro p{font-size:21px;line-height:1.45;text-align:justify;color:var(--grey);font-weight:300;margin-top:10px}
  .intro p.highlight{font-weight:700;color:var(--ink);text-align:left;margin-top:14px}
  .down-btn{display:block;margin-top:18px}

  .advantages{position:absolute;left:0;right:0;top:560px;bottom:0;background:var(--green);
    clip-path:polygon(0 70px,100% 0,100% 100%,0 100%);color:var(--white);padding:150px 150px 0}
  .advantages h2{font-size:30px;font-weight:800;letter-spacing:1px;text-align:center;margin-bottom:40px}
  .adv-list{list-style:none;display:flex;flex-direction:column;gap:26px}
  .adv-list li{display:flex;gap:18px;align-items:flex-start;font-size:19px;line-height:1.45;font-weight:400}
  .adv-list svg{flex:none;margin-top:3px}
</style>
</head>
<body>
<div class="page">
  <header class="site-header">
    <div class="brand">
      <div class="brand-mark"></div>
      <div class="brand-text"><span class="brand-name">VELQUAR</span><span class="brand-tag">VELQUAR BIOTECNOLOGIA ANIMAL</span></div>
    </div>
    <nav class="main-nav">
      <span>HOME</span><span>A EMPRESA</span><span class="active">SERVIÇOS</span><span>FALE CONOSCO</span>
      <span class="lang"><span class="lang-dot"></span>ENG ▾</span>
    </nav>
  </header>

  <ul class="side-nav">
    <li class="current">FIV BOVINOS</li>
    <li>VANTAGENS</li>
    <li>EXEMPLOS</li>
    <li>ETAPAS</li>
  </ul>

  <section class="intro">
    <h1><span>FIV</span> BOVINOS</h1>
    <p>A produção de embriões FIV (fecundados in vitro) é uma das grandes ferramentas da atualidade para otimizar o uso e disseminação de material genético superior com consequente aumento da produtividade e rentabilidade dos rebanhos de leite e corte.</p>
    <p class="highlight">O Brasil é líder absoluto tendo produzido e transferido para fêmeas receptoras bovinas mais de 270 mil embriões FIV em 2015; este montante constitui mais de 60% de toda a produção mundial.</p>
    <svg class="down-btn" width="34" height="34" viewBox="0 0 34 34"><circle cx="17" cy="17" r="16" fill="var(--green)"/><path d="M17 9v15M11 18l6 6 6-6" stroke="#fff" stroke-width="2.5" fill="none" stroke-linecap="round" stroke-linejoin="round"/></svg>
  </section>

  <section class="advantages">
    <h2>VANTAGENS DA FIV</h2>
    <ul class="adv-list">
      <li><svg width="20" height="20" viewBox="0 0 20 20"><path d="M3 10l5 5 9-10" stroke="#fff" stroke-width="2.5" fill="none"/></svg>A FIV pode encurtar o caminho do melhoramento genético em pelo menos três gerações, o equivalente a mais de 10 anos de seleção.</li>
      <li><svg width="20" height="20" viewBox="0 0 20 20"><path d="M3 10l5 5 9-10" stroke="#fff" stroke-width="2.5" fill="none"/></svg>Intensifica o uso de fêmeas com alto mérito genético, que podem ser trabalhadas (aspiradas) com frequência, gerando assim um grande número de prenhezes.</li>
      <li><svg width="20" height="20" viewBox="0 0 20 20"><path d="M3 10l5 5 9-10" stroke="#fff" stroke-width="2.5" fill="none"/></svg>Otimiza o uso do sêmen sexado e de touros de alto valor, já que uma dose de sêmen pode ser usada para fecundar vários oócitos e gerar muitos embriões ao mesmo tempo.</li>
      <li><svg width="20" height="20" viewBox="0 0 20 20"><path d="M3 10l5 5 9-10" stroke="#fff" stroke-width="2.5" fill="none"/></svg>Possibilita a exploração continuada de doadoras gestantes, idosas e pré-púberes.</li>
    </ul>
  </section>
</div>
</body>
</html>
```